Label design needed for cafe display

Hi,
We need a label designed so that we can label food in our display fridge.
The label would have to be editable, as we have lot's of different food items.. and we change the items often, so I would be constantly updating the labels. I will then be printing each label, and laminating them, then displaying them in our food display fridge.
We would like the label to contain our logo - which I have attached.
I have also attached our menus, so you can get a feel for the designs we like.
An example of what we need on a label:
QUICHE LORRAINE $7.50
With Salad $9.50
Please feel free to ask me any questions.
Printing

```html
<!DOCTYPE html>
<html lang="en">
<head>
<meta charset="utf-8">
<title>Harbour Lane – Display Fridge Label</title>
<link rel="stylesheet" href="https://fonts.googleapis.com/css2?family=Bebas+Neue&family=Cabin:wght@400&display=swap">
<style>
  :root {
    --canvas: #ffffff;
    --butter: #f7f3a0;
    --cocoa: #3e3333;
    --cream-text: #ffffff;
  }
  html, body {
    margin: 0;
    padding: 0;
    width: 1200px;
    height: 1000px;
    overflow: hidden;
    background: var(--canvas);
  }
  .canvas {
    position: relative;
    width: 1200px;
    height: 1000px;
  }
  .food-label {
    position: absolute;
    left: 130px;
    top: 290px;
    width: 940px;
    height: 420px;
    background: var(--butter);
    overflow: hidden;
  }
  .food-label__wave {
    position: absolute;
    inset: 0;
    width: 940px;
    height: 420px;
  }
  .brand-badge {
    position: absolute;
    left: 78px;
    top: 80px;
    width: 194px;
    height: 194px;
    border-radius: 50%;
    background: var(--cocoa);
    display: flex;
    flex-direction: column;
    align-items: center;
    justify-content: center;
    color: var(--cream-text);
    font-family: "Cabin", sans-serif;
    font-weight: 400;
    font-size: 23px;
    letter-spacing: 3px;
    line-height: 1.15;
    text-align: center;
  }
  .price-list {
    position: absolute;
    left: 284px;
    width: 600px;
    top: 92px;
    margin: 0;
    padding: 0;
    list-style: none;
    font-family: "Bebas Neue", sans-serif;
    font-size: 76px;
    line-height: 86px;
    color: var(--cocoa);
    text-align: center;
  }
  .price-list__item {
    display: flex;
    justify-content: center;
    gap: 34px;
    white-space: nowrap;
  }
  .contact-line {
    position: absolute;
    left: 0;
    right: 0;
    bottom: 22px;
    margin: 0;
    text-align: center;
    font-family: "Cabin", sans-serif;
    font-size: 17px;
    color: var(--cream-text);
  }
</style>
</head>
<body>
  <main class="canvas">
    <section class="food-label">
      <svg class="food-label__wave" viewBox="0 0 940 420" aria-hidden="true">
        <path d="M0 287 C 180 330 360 355 460 347 C 610 338 770 270 940 262 L 940 420 L 0 420 Z" fill="var(--cocoa)"/>
      </svg>

      <div class="brand-badge">
        <span>HARBOUR</span>
        <span>LANE</span>
      </div>

      <ul class="price-list">
        <li class="price-list__item"><span>Quiche Lorraine</span><span>$7.50</span></li>
        <li class="price-list__item"><span>With Salad</span><span>$9.50</span></li>
      </ul>

      <p class="contact-line">Visit us instore to discuss catering options, or call 0400 246 810 or email hello@harbourlanekitchen.com</p>
    </section>
  </main>
</body>
</html>
```